Looking for a modern website banner design

Corvella Fieldmark Consultants looking for the development of the main banner of the website. The project description and photos are included in the upload files.

```html
<!DOCTYPE html>
<html lang="en">
<head>
<meta charset="utf-8">
<title>Corvella Fieldmark Consultants — Home Banner</title>
<link rel="stylesheet" href="https://fonts.googleapis.com/css2?family=Mulish:wght@200;300;400;700&family=Raleway:wght@200;400&family=Open+Sans:wght@400&display=swap">
<style>
  :root {
    --page-bg: #efefef;
    --panel: #ffffff;
    --brand-blue: #1a6fc4;
    --nav-text: #777777;
    --ink: #111111;
    --body-text: #666666;
    --muted: #555555;
    --rule: #e6e6e6;
    --photo-deep: #1f3a8a;
    --photo-mid: #4f78c8;
  }
  * { box-sizing: border-box; margin: 0; padding: 0; }
  html, body { width: 1200px; height: 913px; overflow: hidden; background: var(--page-bg); }
  .site {
    position: absolute; left: 118px; top: 0; width: 964px; height: 913px;
    background: var(--panel); overflow: hidden;
    font-family: "Mulish", sans-serif;
  }
  .topbar { position: absolute; left: 0; top: 0; width: 100%; height: 35px; border-top: 1px solid #333; }
  .brand {
    position: absolute; left: 60px; top: 8px; display: flex; align-items: center; gap: 6px;
    font-weight: 700; font-size: 16px; color: var(--brand-blue); letter-spacing: .5px;
  }
  .brand-dot { width: 10px; height: 10px; border-radius: 50%; background: var(--brand-blue); }
  .nav { position: absolute; right: 58px; top: 14px; display: flex; gap: 23px; font-size: 7.5px; letter-spacing: 1px; color: var(--nav-text); }
  .nav .nav-cta { color: #6a9fd6; }
  .hero { position: absolute; left: 0; top: 35px; width: 964px; height: 454px; }
  .hero-photo {
    position: absolute; inset: 0;
    background:
      linear-gradient(180deg, rgba(31,58,138,.85) 0%, rgba(79,120,200,.75) 50%, rgba(223,232,246,.95) 75%, #f4f7fc 100%),
      linear-gradient(90deg, var(--photo-mid), var(--photo-deep));
  }
  .hero-veil { position: absolute; left: 0; top: 0; }
  .hero-title { position: absolute; left: 32px; top: 50px; font-weight: 200; font-size: 56px; line-height: 1; color: var(--ink); letter-spacing: -.5px; }
  .testimonial {
    position: absolute; left: 32px; top: 130px; width: 330px;
    font-size: 13.4px; line-height: 20px; color: var(--ink); letter-spacing: -.1px;
    text-decoration: underline; text-underline-offset: 3px; text-decoration-thickness: 1px;
  }
  .athlete { position: absolute; left: 32px; top: 254px; font-size: 14px; line-height: 19px; }
  .athlete-name { display: inline-block; background: var(--brand-blue); color: #fff; font-weight: 700; padding: 0 3px; }
  .athlete-team { display: block; color: var(--muted); padding-left: 2px; }
  .btn-more {
    position: absolute; left: 31px; top: 371px; width: 137px; height: 42px;
    border: 2px solid var(--brand-blue); background: #fff;
    font-size: 16px; color: var(--ink); display: flex; align-items: center; justify-content: center; letter-spacing: .3px;
  }
  .hero-edge { position: absolute; left: 0; top: 489px; width: 100%; height: 3px; background: #eeeeee; }
  .intro { position: absolute; left: 0; top: 529px; width: 100%; text-align: center; }
  .intro-heading {
    font-family: "Raleway", sans-serif; font-weight: 400; font-size: 16px; letter-spacing: 4.6px;
    color: var(--brand-blue); line-height: 28px; white-space: nowrap;
  }
  .intro-body {
    font-family: "Open Sans", sans-serif; font-size: 11.6px; line-height: 19.7px; color: var(--body-text);
    width: 690px; margin: 27px auto 0;
  }
  .intro-quote { font-family: "Open Sans", sans-serif; font-size: 9px; line-height: 17px; color: var(--body-text); margin-top: 19px; }
  .divider { position: absolute; left: 0; top: 825px; width: 100%; height: 1px; background: var(--rule); }
  .process-title {
    position: absolute; left: 0; top: 888px; width: 100%; text-align: center;
    font-family: "Raleway", sans-serif; font-weight: 200; font-size: 34px; letter-spacing: 8px; color: var(--ink);
  }
  .process-title sup { font-size: 12px; letter-spacing: 0; }
</style>
</head>
<body>
  <div class="site">
    <header class="topbar">
      <div class="brand"><span class="brand-dot"></span>FIELDMARK</div>
      <nav class="nav">
        <span>ABOUT</span><span>FEATURES</span><span>USES</span>
        <span class="nav-cta">☆ TRY FIELDMARK AD</span><span>🔒︎ LOGIN</span>
      </nav>
    </header>

    <section class="hero">
      <div class="hero-photo" role="img" aria-label="Hockey players on the ice celebrating in front of a cheering arena crowd, tinted blue"></div>
      <svg class="hero-veil" width="440" height="454" viewBox="0 0 440 454" aria-hidden="true">
        <path d="M0 0 H225 L429 210 Q438 225 429 240 L225 454 H0 Z" fill="rgba(255,255,255,0.86)"/>
      </svg>
      <h1 class="hero-title">Fieldmark</h1>
      <p class="testimonial">has provided support that has allowed me to develop as a person and an athlete.&nbsp; The S.T.R.I.D.E.™ process allowed me to stay focused on attainable goals each season and progress from Junior to College and now Professional Hockey.</p>
      <div class="athlete">
        <span class="athlete-name">Marek Dolan</span>
        <span class="athlete-team">Riverton Falcons</span>
        <span class="athlete-team">Atlantic Ice League</span>
      </div>
      <div class="btn-more">MORE INFO</div>
    </section>
    <div class="hero-edge"></div>

    <section class="intro">
      <h2 class="intro-heading">THE EFFECTIVE WAY TO SUCCESSFULLY DEVELOP AN<br>ATHLETE</h2>
      <p class="intro-body">Success in life is not possible without ongoing or infinite personal development. New levels of success bring new challenges or higher skill levels to maintain success. This is obvious in Athlete Development, as success brings us to higher levels in our sport and/or higher expectations. Ongoing Athlete Development is only possible with the creation and execution of an Athlete Development plan and that is what Fieldmark AD specializes in.</p>
      <p class="intro-quote">“Setting the goal is not the main thing, it is deciding how you will go about achieving it and staying with that plan.”<br>Hal Brenner Hall of Fame Football Coach of the Lakeshore Rams</p>
    </section>

    <div class="divider"></div>
    <h2 class="process-title">STRIDE<sup>TM</sup></h2>
  </div>
</body>
</html>
```